Business cards for Remote DBA team

Business cards for team offering database administration, consultation, machine learning and AI services. As of now team is using both
www.korvilnet.cz and www.brestmoorlab.cz URLs

Target Market(s)

IT managers

Industry/Entity Type

It Professional

Contact Information for Business Card

Should include logo
name, email, phone, twitter tag

Font styles to use
Sans Serif

Colors

Designer to choose colors to be used in the design.

```html
<!DOCTYPE html>
<html lang="en">
<head>
<meta charset="utf-8">
<title>Brestmoor Lab – Business Cards</title>
<link rel="stylesheet" href="https://fonts.googleapis.com/css2?family=Lato:wght@400;700&family=Montserrat:wght@700&display=swap">
<style>
  :root {
    --backdrop: #e8e5e0;
    --card: #ffffff;
    --blue: #1688c8;
    --grey-line: #a7a7a7;
    --grey-band: #9b9b9b;
    --text: #333333;
    --icon-blue: #2f8fcd;
    --pattern: #f3f7fa;
    --stack-top: #8c9bcf;
    --stack-dark: #3b4452;
  }
  * { box-sizing: border-box; margin: 0; padding: 0; }
  html, body { width: 900px; height: 1200px; overflow: hidden; }
  body {
    background: var(--backdrop);
    position: relative;
    font-family: "Lato", Arial, sans-serif;
    color: var(--text);
  }
  .card {
    position: absolute;
    left: 87px;
    width: 733px;
    background: var(--card);
    border-radius: 22px;
    overflow: hidden;
    box-shadow: 0 3px 8px rgba(0,0,0,.18);
  }
  .card-front { top: 137px; height: 426px; border-bottom: 6px solid var(--blue); }
  .card-back { top: 632px; height: 430px; }

  .brand {
    position: absolute;
    display: flex;
    align-items: center;
    font-family: "Montserrat", Arial, sans-serif;
    font-weight: 700;
    color: var(--blue);
    line-height: 1;
  }
  .brand-dot { border-radius: 50%; background: var(--blue); flex: none; }
  .card-front .brand { left: 30px; top: 70px; font-size: 38px; gap: 16px; }
  .card-front .brand-dot { width: 30px; height: 30px; }

  .service-art {
    position: absolute;
    right: 28px; top: 78px;
    width: 200px; height: 94px;
    border-radius: 14px;
    background: linear-gradient(180deg, var(--stack-top), var(--stack-dark));
    opacity: .85;
  }

  .divider {
    position: absolute;
    left: 28px; right: 27px; top: 283px;
    height: 2px; background: var(--grey-line);
  }

  .contacts { position: absolute; left: 28px; top: 300px; list-style: none; }
  .contacts li {
    display: flex; align-items: center;
    height: 28px; font-size: 17px; letter-spacing: .2px;
  }
  .contacts svg { width: 16px; height: 16px; margin-right: 12px; fill: var(--icon-blue); flex: none; }

  .person { position: absolute; right: 27px; top: 296px; text-align: right; }
  .person-name {
    font-family: "Montserrat", Arial, sans-serif;
    font-weight: 700; font-size: 27px; color: var(--blue); letter-spacing: .5px;
  }
  .person-role { font-size: 17px; margin-top: 4px; letter-spacing: .3px; }

  .social {
    position: absolute; right: 27px; top: 384px;
    display: flex; align-items: center; gap: 12px; font-size: 17px;
  }
  .social-dot { width: 20px; height: 20px; border-radius: 50%; background: var(--icon-blue); }

  .pattern-field { position: absolute; inset: 0 0 64px 0; background: var(--pattern); }
  .card-back .brand {
    left: 0; right: 0; top: 170px; justify-content: center;
    font-size: 52px; gap: 20px;
  }
  .card-back .brand-dot { width: 40px; height: 40px; }
  .web-band {
    position: absolute; left: 0; right: 0; bottom: 0; height: 64px;
    background: var(--grey-band);
    display: flex; align-items: center; justify-content: center;
    color: #fff; font-weight: 700; font-size: 17px; gap: 16px;
  }
  .web-band .host { color: var(--blue); }
</style>
</head>
<body>

<section class="card card-front">
  <div class="brand"><span class="brand-dot"></span>Brestmoor Lab</div>
  <div class="service-art" role="img" aria-label="Database stack illustrations with gear and cloud"></div>

  <div class="divider"></div>

  <ul class="contacts">
    <li>
      <svg viewBox="0 0 16 16" aria-hidden="true"><path d="M4 0h8a1 1 0 0 1 1 1v14a1 1 0 0 1-1 1H4a1 1 0 0 1-1-1V1a1 1 0 0 1 1-1zm1 2v10h6V2zm3 11a1 1 0 1 0 0 2 1 1 0 0 0 0-2z"/></svg>
      000 000 0000
    </li>
    <li>
      <svg viewBox="0 0 16 16" aria-hidden="true"><path d="M0 3h16v10H0zM1.5 4.2 8 9l6.5-4.8V4.5H1.5z" /></svg>
      tomas@brestmoorlab.cz
    </li>
    <li>
      <svg viewBox="0 0 16 16" aria-hidden="true"><path d="M8 0a8 8 0 1 0 0 16A8 8 0 0 0 8 0zm5.9 7h-2.5a12 12 0 0 0-.9-4.6A6 6 0 0 1 13.9 7zM8 2c.6.8 1.3 2.6 1.4 5H6.6C6.7 4.6 7.4 2.8 8 2zM5.5 2.4A12 12 0 0 0 4.6 7H2.1a6 6 0 0 1 3.4-4.6zM2.1 9h2.5c.1 1.7.4 3.3.9 4.6A6 6 0 0 1 2.1 9zM8 14c-.6-.8-1.3-2.6-1.4-5h2.8c-.1 2.4-.8 4.2-1.4 5zm2.5-.4c.5-1.3.8-2.9.9-4.6h2.5a6 6 0 0 1-3.4 4.6z"/></svg>
      www.korvilnet.cz
    </li>
    <li>
      <svg viewBox="0 0 16 16" aria-hidden="true"><path d="M8 0a8 8 0 1 0 0 16A8 8 0 0 0 8 0zm5.9 7h-2.5a12 12 0 0 0-.9-4.6A6 6 0 0 1 13.9 7zM8 2c.6.8 1.3 2.6 1.4 5H6.6C6.7 4.6 7.4 2.8 8 2zM5.5 2.4A12 12 0 0 0 4.6 7H2.1a6 6 0 0 1 3.4-4.6zM2.1 9h2.5c.1 1.7.4 3.3.9 4.6A6 6 0 0 1 2.1 9zM8 14c-.6-.8-1.3-2.6-1.4-5h2.8c-.1 2.4-.8 4.2-1.4 5zm2.5-.4c.5-1.3.8-2.9.9-4.6h2.5a6 6 0 0 1-3.4 4.6z"/></svg>
      www.brestmoorlab.cz
    </li>
  </ul>

  <div class="person">
    <div class="person-name">TOMAS VRANA</div>
    <div class="person-role">Data Platform Architect</div>
  </div>

  <div class="social"><span class="social-dot"></span>@halvorik</div>
</section>

<section class="card card-back">
  <div class="pattern-field" role="img" aria-label="Faint binary digit background pattern"></div>
  <div class="brand"><span class="brand-dot"></span>Brestmoor Lab</div>
  <div class="web-band">
    <span>www.<span class="host">korvilnet</span>.cz</span>
    <span>|</span>
    <span>www.<span class="host">brestmoorlab</span>.cz</span>
  </div>
</section>

</body>
</html>
```